Industrial & commercial facility maintenance flyer

Design a 2 sided flyer that outlines our core business unit services. One side shall be for our industrial maintenance division while the other will be focused on our commercial maintenance division.

Media from website here: https://files.vornelbox.net/share/7Kq29XzPw4RtLmYc8NdHe5JbVa

Target Market(s)

Industrial and commercial facility maintenance companies and professionals

Industry/Entity Type

Maintenance

Font styles to use
Serif

Colors
ffffff
2f73b4
0455a3
cfdfed

Requirements
Must have
• Several photos of each applicable service. Reference existing website (www.trelcorp.com). Use of the blue and grey scheme of our current logo.
Nice to have
• Our logo design across the top with our contact information on the bottom.

```html
<!DOCTYPE html>
<html lang="en">
<head>
<meta charset="utf-8">
<title>Trelcorp Maintenance Solutions – Two-Sided Flyer</title>
<link href="https://fonts.googleapis.com/css2?family=Oswald:wght@400;500;600&family=Open+Sans:ital,wght@0,400;0,600;0,700;1,600&display=swap" rel="stylesheet">
<style>
:root{
  --blue:#0455a3;
  --blue-mid:#2f73b4;
  --blue-deep:#0a3d86;
  --blue-pale:#cfdfed;
  --white:#ffffff;
  --grey:#5f6063;
  --grey-dark:#44464a;
  --stage:#8a8b8d;
  --ink:#2b2b2b;
}
*{margin:0;padding:0;box-sizing:border-box}
html,body{width:1200px;height:3427px;overflow:hidden}
body{background:var(--stage);font-family:"Open Sans",Arial,sans-serif;position:relative}
.page{position:absolute;left:29px;width:1142px;background:var(--white);overflow:hidden;box-shadow:0 6px 18px rgba(0,0,0,.45)}
.page--industrial{top:29px;height:1622px}
.page--retail{top:1742px;height:1656px}
.abs{position:absolute}
.photo{position:absolute;overflow:hidden}
.photo--round{border-radius:50%;border:14px solid var(--white)}
.brand{position:absolute;display:flex;align-items:center;gap:16px;height:74px}
.brand__mark{width:74px;height:74px;border-radius:50%;background:var(--blue);flex:none}
.brand__name{font-family:"Open Sans",Arial,sans-serif;font-weight:600;color:var(--blue);font-size:32px;line-height:1;white-space:nowrap;margin-top:-18px}
.brand__tag{position:absolute;left:90px;top:48px;font-family:"Oswald",Arial,sans-serif;font-size:14px;letter-spacing:4px;color:var(--grey);white-space:nowrap}
.band{position:absolute;left:0;width:100%}
.headline{font-family:"Oswald",Arial,sans-serif;color:var(--white);text-transform:uppercase;font-weight:500;line-height:1.15}
.tagline{font-family:"Open Sans",Arial,sans-serif;font-style:italic;font-weight:600;color:var(--white);font-size:30px}
.copy{font-size:13px;line-height:1.4;color:var(--ink);text-align:justify}
.copy p{margin-bottom:10px}
.copy--light{color:var(--white);font-size:16px;line-height:1.42}
.cta{position:absolute;display:flex;flex-direction:column;justify-content:center;padding-left:60px;color:var(--white)}
.cta__label{font-size:27px}
.cta__url{font-size:26px;font-weight:700}
.section-title{font-family:"Oswald",Arial,sans-serif;color:var(--blue);text-transform:uppercase;line-height:1}
.section-title__main{font-size:58px;font-weight:500}
.section-title__sub{font-size:32px;font-weight:500;color:var(--blue-mid);margin-top:8px}
.social{position:absolute;display:flex;align-items:center;justify-content:flex-end;gap:14px;padding-right:28px;background:var(--blue);color:var(--white);font-size:30px}
.social__dot{width:48px;height:48px;border-radius:50%;background:var(--white)}
.social__lead{margin-right:10px}
.social__badge{position:absolute;left:26px;top:50%;transform:translateY(-50%);width:58px;height:58px;border-radius:50%;border:3px solid var(--white)}
</style>
</head>
<body>

<!-- Side one: industrial -->
<section class="page page--industrial">
  <div class="band" style="top:235px;height:455px;background:linear-gradient(120deg,var(--blue-deep),var(--blue) 55%,var(--blue-mid));"></div>

  <div class="photo photo--round" role="img" aria-label="Technician in blue overalls and yellow gloves tightening a valve with a wrench" style="left:520px;top:-110px;width:600px;height:600px;background:radial-gradient(circle at 60% 55%,#9fb0bf,#2c4f86 60%,#1b3566);"></div>

  <div class="brand" style="left:40px;top:78px">
    <div class="brand__mark"></div>
    <div class="brand__name">Trelcorp Maintenance</div>
    <div class="brand__tag">INDUSTRIAL · COMMERCIAL · RETAIL</div>
  </div>

  <div class="abs" style="left:52px;top:470px;width:480px">
    <h1 class="headline" style="font-size:40px">Facility Maintenance &amp;<br>Management Solutions</h1>
    <div class="tagline" style="margin-top:4px">“Maintaining Your Business”</div>
  </div>

  <svg class="abs" style="left:0;top:665px" width="590" height="80" viewBox="0 0 590 80" aria-hidden="true">
    <polygon points="0,0 590,0 540,80 0,80" fill="var(--grey)"/>
  </svg>
  <h2 class="headline abs" style="left:40px;top:680px;font-size:30px;font-weight:400">Industrial Maintenance Solutions</h2>

  <div class="abs" style="left:0;top:745px;width:590px;height:200px;background:linear-gradient(180deg,var(--grey-dark),var(--grey))"></div>
  <div class="copy copy--light abs" style="left:40px;top:755px;width:510px">
    Our industrial maintenance teams work in the field to handle your needs as quickly as possible, whether to get your critical broken or malfunctioning equipment going again or to support scheduled downtime. We specialize in industrial maintenance, conveyor repair, and overhead door repair, but our industrial services aren’t limited to those services. Others include equipment repairs, installation, and adjustment, just to name a few.
  </div>

  <div class="cta" style="left:583px;top:775px;width:559px;height:111px;background:var(--blue)">
    <span class="cta__label">Get Your Maintenance Solution</span>
    <span class="cta__url">www.trelcorp.com</span>
  </div>

  <div class="photo" role="img" aria-label="Wide view of a factory floor with yellow overhead cranes and machinery" style="left:0;top:945px;width:540px;height:677px;border-radius:0 340px 340px 0;background:linear-gradient(160deg,#c9b58a,#7f7a6d 45%,#3f5f86);"></div>

  <div class="abs" style="left:590px;top:950px;width:520px">
    <div class="section-title">
      <div class="section-title__main" style="font-size:50px">Industrial Maintenance</div>
      <div class="section-title__sub" style="font-size:28px">Services You Can Rely On</div>
    </div>
    <div class="copy" style="margin-top:14px;font-size:12.5px;line-height:1.36">
      <p>Trelcorp Maintenance Solutions has been Atlanta’s trusted industrial and commercial maintenance solution for over 10 years. Our industrial teams are available 24/7 for equipment maintenance, installation, or repair, and can be onsite within 4 hours.</p>
      <p>We provide conveyor system repair and overhead door repair and maintenance, but our services don’t end there. We cater to your needs to provide exactly what services you want. Other services we offer include plant maintenance, equipment installation and relocation, and repairs of all types of process and manufacturing equipment. We also offer facility safety consultations.</p>
      <p>Trelcorp Maintenance Solutions has teams of welders, millwrights, mechanics, carpenters, and more standing ready to support your operation. The welders are certified and provide fabrication in carbon steel, stainless steel, structural steel, sheet metal, aluminum, and chrome alloy. Our millwrights and mechanics safely move, assemble, and install machinery with exact positioning and rigging.</p>
      <p>We provide equipment repair services to many local industries. Services include repair of bearing boxes, repair/replacement of worn shafts and production equipment, hydraulic system repair, broken bolt removal, and much more.</p>
    </div>
  </div>

  <div class="social" style="left:500px;top:1483px;width:642px;height:84px">
    <span class="social__lead">Follow us on</span>
    <span class="social__dot"></span><span class="social__dot"></span><span class="social__dot"></span>
  </div>
</section>

<!-- Side two: retail & commercial -->
<section class="page page--retail">
  <div class="band" style="top:322px;height:648px;background:linear-gradient(120deg,var(--blue-deep),var(--blue) 50%,var(--blue-mid));"></div>

  <div class="photo photo--round" role="img" aria-label="Technician with tool belt carrying a toolbox beside a service van" style="left:-60px;top:-60px;width:500px;height:500px;background:radial-gradient(circle at 45% 50%,#c4ccd6,#3c5e95 55%,#e3e6ea);"></div>

  <div class="brand" style="left:640px;top:74px">
    <div class="brand__mark"></div>
    <div class="brand__name">Trelcorp Maintenance</div>
    <div class="brand__tag">INDUSTRIAL · COMMERCIAL · RETAIL</div>
  </div>

  <svg class="abs" style="left:620px;top:214px" width="522" height="108" viewBox="0 0 522 108" aria-hidden="true">
    <polygon points="40,0 522,0 522,108 0,108" fill="var(--grey)"/>
  </svg>
  <div class="cta" style="left:655px;top:214px;width:487px;height:108px">
    <span class="cta__label">Get Your Maintenance Solution</span>
    <span class="cta__url">www.trelcorp.com</span>
  </div>

  <div class="abs" style="left:58px;top:574px;width:500px">
    <h2 class="headline" style="font-size:38px;font-weight:400">Retail &amp; Commercial<br>Maintenance Solutions</h2>
    <div class="copy copy--light" style="margin-top:14px">
      Trelcorp Maintenance Solutions knows how important it is to convert window shoppers to paying customers and to move inventory off your shelves. We ensure that your business is always looking its best with our cost-effective maintenance programs and crews available 24/7 to take care of any equipment or facility malfunction as quickly as possible.
    </div>
  </div>

  <div class="photo photo--round" role="img" aria-label="Technician in hard hat and safety vest servicing a ceiling air conditioning unit" style="left:583px;top:560px;width:552px;height:552px;background:radial-gradient(circle at 50% 45%,#e9e3d4,#b8a98a 50%,#5b6f8c);"></div>

  <div class="abs" style="left:58px;top:1070px;width:640px">
    <div class="section-title">
      <div class="section-title__main">Retail Maintenance</div>
      <div class="section-title__sub">Services You Can Rely On</div>
    </div>
  </div>
  <div class="copy abs" style="left:58px;top:1190px;width:565px">
    <p>Trelcorp Maintenance Solutions provides services to stand-alone stores and big box stores alike, malls, nightclubs, and more. We work to enhance your image by taking preventative measures, like inspecting equipment for signs of wear or failing components. We service equipment as needed, measuring either by usage or manufacturer recommendations. After maintenance and repairs, our technicians provide an in-depth report on equipment conditions, analyze equipment failure, and discuss future prevention.</p>
    <p>Customers may not realize how much work and effort goes into maintaining a functional well-kept business, but Trelcorp Maintenance does. For your convenience, we offer a vast range of services to handle any issues that may occur or to help you expand your business, whether adding on to your existing location or moving to a new one.</p>
    <p>We install doors, restroom partitions, storefronts, flooring, and plumbing. Repairs include doors, storefronts, flooring, building exteriors, plumbing, appliances, fencing, and loading docks. We take care of landscaping, snow removal, irrigation systems, pest control, and other seasonal maintenance as need be when the weather changes.</p>
  </div>

  <div class="social" style="left:643px;top:1490px;width:499px;height:84px">
    <span class="social__badge"></span>
    <span class="social__lead">Follow us on</span>
    <span class="social__dot"></span><span class="social__dot"></span><span class="social__dot"></span>
  </div>
</section>

</body>
</html>
```